GPS SALES

Lopoking to design a website for my company " Marbury Designs"
Our slogan is "GPS that's shaped to suit"

I sell in dash gps systems for cars that are built into the dash board. No gaps after install. designed specifically for specific cars.
I have products for all manufacturers...

Want lots of colour!
Online ordering system with payment options online

This is a sales only website....

A site that sells similar products is:
http://e.vantelmo.cn/
I want my website to be very similar to this one.

Im basically selling these products here in australia. So I really want something "australian themed" (kangaroo or koala or australia map....)this kind of thing

Looking to attract business from car dealerships and the public.

I have attached a copy of my brochure, and some of the products I sell

```html
<!DOCTYPE html>
<html lang="en">
<head>
<meta charset="utf-8">
<title>Marbury Designs — In Dash GPS</title>
<link href="https://fonts.googleapis.com/css2?family=Open+Sans:wght@300;400;600;700&display=swap" rel="stylesheet">
<style>
  :root {
    --blue: #0a5cad;
    --blue-bright: #0f6fc6;
    --orange: #f7892d;
    --orange-deep: #f26c0d;
    --ink: #4a4a4a;
    --muted: #8a8a8a;
    --stage: #a9a9a9;
    --white: #ffffff;
  }
  * { box-sizing: border-box; margin: 0; padding: 0; }
  html, body { width: 1110px; height: 1200px; overflow: hidden; }
  body { background: var(--stage); font-family: "Open Sans", sans-serif; color: var(--ink); position: relative; }

  .page {
    position: absolute; left: 152px; top: 27px; width: 808px; height: 1111px;
    background: var(--white); border: 4px solid var(--blue-bright); border-radius: 8px;
    box-shadow: 8px 8px 0 var(--orange);
  }
  .brand { position: absolute; left: 26px; top: 22px; display: flex; align-items: center; gap: 10px; }
  .brand-mark { width: 40px; height: 40px; border-radius: 6px; background: var(--blue-bright); }
  .brand-name { font-size: 26px; font-weight: 700; color: var(--blue); line-height: 1; }
  .social { position: absolute; right: 40px; top: 27px; display: flex; gap: 7px; }
  .social span { width: 26px; height: 26px; border-radius: 50%; background: var(--blue); display: block; }

  .ribbon {
    position: absolute; left: -19px; top: 75px; width: 845px; height: 32px;
    background: var(--orange); border-radius: 10px 10px 14px 14px;
    display: flex; align-items: center; z-index: 2;
  }
  .slogan { color: var(--white); font-weight: 700; font-size: 16px; padding-left: 36px; flex: 1; }
  .nav { display: flex; height: 100%; padding-right: 30px; }
  .nav a { color: var(--white); text-decoration: none; font-size: 13.5px; display: flex; align-items: center; padding: 0 19px; border-left: 1px solid rgba(255,255,255,.35); }
  .nav a:first-child { border-left: 0; }
  .nav a.active { background: var(--blue-bright); padding: 0 17px; }

  .hero {
    position: absolute; left: 0; top: 106px; width: 800px; height: 378px;
    background: linear-gradient(100deg, #2b2e33 0%, #5a5f66 35%, #8e9298 55%, #3c3f44 80%, #1f2124 100%);
  }
  .hero-copy { position: absolute; left: 446px; top: 64px; width: 330px; color: var(--white); }
  .hero-copy h1 { font-size: 34px; line-height: 41px; font-weight: 700; }
  .hero-copy p { font-size: 14px; line-height: 22px; font-weight: 600; margin-top: 16px; }
  .btn { display: inline-block; background: var(--orange-deep); color: var(--white); text-decoration: none; }
  .hero-copy .btn { margin-top: 15px; width: 142px; height: 41px; line-height: 41px; text-align: center; font-size: 15px; }
  .dots { position: absolute; left: 364px; top: 442px; display: flex; gap: 8px; }
  .dots span { width: 14px; height: 14px; border-radius: 50%; background: var(--blue-bright); border: 2px solid var(--white); }
  .dots span.on { background: var(--orange); }

  .col { position: absolute; top: 512px; width: 240px; }
  .col h2 { font-size: 19px; font-weight: 700; color: var(--blue); }
  .col .shot { width: 237px; height: 136px; margin-top: 11px; border: 1px solid #ddd; }
  .col p { font-size: 11px; line-height: 17.5px; margin-top: 6px; color: var(--ink); }
  .col a { color: var(--orange-deep); font-style: italic; font-size: 10px; margin-left: 8px; }
  .shot-products { background: linear-gradient(135deg, #e6e7e8, #9da3a6 60%, #d7d9da); }
  .shot-services { background: linear-gradient(135deg, #3a3d40, #a7abae 55%, #e4e5e6); }
  .quote-mark { color: var(--orange-deep); font-size: 44px; font-weight: 700; line-height: 30px; float: left; margin: 8px 8px 0 0; height: 24px; font-family: Georgia, serif; }
  .testimonial p { font-size: 12.5px; line-height: 20px; margin-top: 11px; font-weight: 300; color: #555; }
  .author { font-size: 12.5px; color: var(--orange-deep); font-weight: 600; margin-top: 11px; }
  .author-place { font-size: 9px; color: var(--muted); }

  .about { position: absolute; left: 39px; top: 797px; width: 475px; }
  .about h2 { font-size: 24px; font-weight: 700; color: var(--blue); }
  .about h2 span { color: var(--orange-deep); }
  .about p { font-size: 13px; line-height: 20px; font-weight: 300; color: #555; margin-top: 14px; }
  .about p + p { margin-top: 8px; }
  .about .btn { margin-top: 34px; width: 110px; height: 31px; line-height: 31px; text-align: center; font-size: 12.5px; box-shadow: 1px 2px 3px rgba(0,0,0,.25); }
  .map { position: absolute; left: 521px; top: 792px; width: 260px; height: 233px; background: var(--blue); border-radius: 40% 45% 38% 50%; }

  .footer {
    position: absolute; left: 0; top: 1067px; width: 800px; height: 38px; background: var(--blue);
    display: flex; align-items: center; color: var(--white); font-size: 11px;
  }
  .copyright { padding-left: 30px; font-weight: 600; flex: 1; letter-spacing: -0.2px; }
  .footer-nav { display: flex; padding-right: 28px; }
  .footer-nav a { color: var(--white); text-decoration: none; margin-left: 39px; font-size: 12px; }
</style>
</head>
<body>
  <div class="page">
    <header>
      <div class="brand"><span class="brand-mark"></span><span class="brand-name">Marbury Designs</span></div>
      <div class="social" aria-label="Social links"><span></span><span></span></div>
      <div class="ribbon">
        <div class="slogan">GPS that's shaped to suit!</div>
        <nav class="nav">
          <a class="active" href="#">Home</a>
          <a href="#">Services</a>
          <a href="#">Products</a>
          <a href="#">About Us</a>
          <a href="#">Contact Us</a>
        </nav>
      </div>
    </header>

    <section class="hero" role="img" aria-label="Car interior with an in-dash GPS head unit and steering wheel">
      <div class="hero-copy">
        <h1>Dash GPS Systems for cars</h1>
        <p>Selling in dash gps systems for cars that are built into the dash board. No gaps after install. designed specifically for specific cars.</p>
        <a class="btn" href="#">Shop Now</a>
      </div>
      <div class="dots"><span></span><span class="on"></span><span></span><span></span></div>
    </section>

    <section class="col" style="left:32px">
      <h2>Our Products</h2>
      <div class="shot shot-products" role="img" aria-label="In-dash GPS units showing navigation maps"></div>
      <p>Our products are designed specifically for spe-cific cars with a wide range of car model and manufacturers <a href="#">learn more &gt;</a></p>
    </section>
    <section class="col" style="left:289px">
      <h2>Services</h2>
      <div class="shot shot-services" role="img" aria-label="Technician with a laptop working inside a car"></div>
      <p>Sed ut perspiciatis unde omnis iste natus error sit voluptatem each &nbsp;sa quae ab illo inventore veritatis et <a href="#">learn more &gt;</a></p>
    </section>
    <section class="col testimonial" style="left:547px; width:230px">
      <h2>Testimonials</h2>
      <p><span class="quote-mark">&ldquo;</span>Aspernatur aut dit aut fugit sedy quia consequtur magnifest doluptatem sequi nesciunt Neque porro quisquam est, qui dolorem ipsum quia. Tus amen lorem ipsum dolore ang bantot modist tempora incidunt ut labore dolore ist magnam aliquat voluptatem.</p>
      <div class="author">Jane Porter</div>
      <div class="author-place">Perth, Western Australia</div>
    </section>

    <section class="about">
      <h2>About Marbury <span>Designs</span></h2>
      <p>Sed ut perspiciatis unde omnis iste natus error sit voluptatem each &nbsp;sa quae ab illo inventore veritatis et quasi architecto bea tae vitae dictarts explicabo. Nemo enim ipsam voluptatem quia volup tas sit.</p>
      <p>Aspernatur aut odit aut fugit sed quia consequuntur magni doluptatem sequi nesciunt Neque porro quisquam est, qui dolorem ipsum quia.</p>
      <a class="btn" href="#">Learn More</a>
    </section>
    <div class="map" role="img" aria-label="Map of Australia with a location pin on Perth"></div>

    <footer class="footer">
      <div class="copyright">Copyright Marbury Designs . All right reserved.</div>
      <nav class="footer-nav">
        <a href="#">Home</a><a href="#">Services</a><a href="#">Products</a><a href="#">About Us</a><a href="#">Contact Us</a>
      </nav>
    </footer>
  </div>
</body>
</html>
```